Advertising brochure for Trail Along Southside

We need a new single sided DL flier for the 2020 season!<br/>This flier is for our tour business. You can find all the details about the tour at our web site http://trailalong.southside.example<br/>The flier needs to grab the tourists attention, explain the tour and give price. I will upload a copy of last year's flier for your reference.<br/>We'd like the flier to match our web site to some extent.<br/>The most up to date information is on the web site and NOT last year's brochure. Use the web site for tour itinerary. We NO LONGER do the "Orchard Walk".<br/>Remember the size is "DL". Please no A4 format etc.<br/>You will be able to source images from:<br/>- Our web site<br/>- Our Chatterbook<br/>- Roamreview<br/>- Quarrel Listings<br/>If you have a particular idea in mind then feel free to contact us and we will try to accommodate your photo request.<br/>Good luck!

Target Market(s)

All ages

Industry/Entity Type

Tourism

Requirements
Must have
• Phone number
• Web Site
• Email address
• Price
Nice to have
• Description of tour and images

```html
<!DOCTYPE html>
<html lang="en">
<head>
<meta charset="utf-8">
<title>Trail Along Southside – Tour Flier</title>
<link href="https://fonts.googleapis.com/css2?family=Bebas+Neue&family=Lato:wght@400;700&family=Montserrat:wght@600;700;900&display=swap" rel="stylesheet">
<style>
  :root{
    --backdrop:#48484b;
    --orange-light:#f9a54a;
    --orange:#f38b2c;
    --orange-deep:#ee7a1f;
    --red:#e8231d;
    --red-orange:#f15a24;
    --yellow:#ffd23c;
    --ink:#1e1e1e;
    --white:#ffffff;
    --footer:#4a4a4a;
  }
  *{box-sizing:border-box;margin:0;padding:0}
  html,body{width:1200px;height:857px;overflow:hidden;background:var(--backdrop)}
  .flier{
    position:absolute;left:400px;top:30px;width:400px;height:796px;overflow:hidden;
    background:
      radial-gradient(ellipse at 50% 15%, #fbb663 0%, transparent 60%),
      linear-gradient(180deg,var(--orange-light) 0%,var(--orange) 45%,var(--orange-deep) 100%);
    font-family:'Lato',sans-serif;color:var(--ink);
    box-shadow:0 10px 30px rgba(0,0,0,.35);
  }
  .dunes{position:absolute;left:0;top:430px;width:400px;height:340px}
  .badge{position:absolute;border-radius:50%;display:flex;flex-direction:column;align-items:center;justify-content:center;text-align:center;
    background:radial-gradient(circle at 40% 35%,#f7763a,var(--red-orange) 70%);border:3px solid #f9a03c}
  .price-badge{left:38px;top:13px;width:130px;height:130px}
  .price-amount{font-family:'Bebas Neue',sans-serif;font-size:62px;line-height:.9;color:var(--white);letter-spacing:-1px}
  .price-unit{font-family:'Bebas Neue',sans-serif;font-size:15px;background:var(--yellow);color:var(--red-orange);border-radius:8px;padding:1px 6px;margin-top:2px}
  .price-kids{font-family:'Montserrat',sans-serif;font-weight:700;font-size:10px;color:var(--white);margin-top:3px}
  .price-free{font-family:'Montserrat',sans-serif;font-weight:700;font-size:5px;color:var(--white);margin-top:1px}
  .brand-badge{left:230px;top:10px;width:132px;height:132px}
  .brand-name{font-family:'Montserrat',sans-serif;font-weight:700;font-size:13px;line-height:1.2;color:var(--white);padding:0 14px}
  .headline{position:absolute;left:25px;top:158px;font-family:'Montserrat',sans-serif;font-weight:900;font-size:45px;line-height:.9;color:var(--red);letter-spacing:-.5px}
  .intro{position:absolute;left:18px;width:364px;top:243px;text-align:center;font-family:'Montserrat',sans-serif;font-weight:600;font-size:10.6px;line-height:1.25}
  .intro .site{font-weight:700;color:var(--red)}
  .stop{position:absolute}
  .stop h2{font-family:'Bebas Neue',sans-serif;font-weight:400;font-size:19px;line-height:1;margin-bottom:2px}
  .stop p{font-size:9.4px;line-height:1.3}
  .stop.right-text{text-align:right}
  .photo{position:absolute;width:115px;height:72px;border:5px solid var(--white);border-radius:6px;box-shadow:0 2px 5px rgba(0,0,0,.2)}
  .footer{position:absolute;left:0;bottom:0;width:400px;height:33px;background:var(--footer);display:flex;align-items:center;gap:8px;padding-left:30px;
    font-family:'Montserrat',sans-serif;font-weight:700;font-size:11.5px;color:var(--white)}
  .footer svg{flex:none}
  .footer .phone{margin-left:10px}
</style>
</head>
<body>
<main class="flier">
  <svg class="dunes" viewBox="0 0 400 340" preserveAspectRatio="none" aria-hidden="true">
    <path d="M0 70 L60 40 L120 55 L190 20 L260 50 L330 15 L400 35 L400 340 L0 340Z" fill="#ef8425" opacity=".6"/>
    <path d="M0 150 L80 120 L150 140 L230 110 L300 135 L400 105 L400 340 L0 340Z" fill="#ec7a1e" opacity=".6"/>
  </svg>

  <div class="badge price-badge">
    <div class="price-amount">£50</div>
    <div class="price-unit">PER PERSON</div>
    <div class="price-kids">KIDS HALF PRICE</div>
    <div class="price-free">CHILDREN UNDER 5 FREE</div>
  </div>
  <div class="badge brand-badge">
    <div class="brand-name">Trail Along Southside</div>
  </div>

  <h1 class="headline">TRAIL. ALONG.<br>SOUTHSIDE.</h1>
  <p class="intro">Join our guide in a unique tag-along adventure around Redstone Flats. Tour runs daily at 9am and for approx 3 hours.<br>Book at <span class="site">trailalong.southside.example</span></p>

  <section class="stop right-text" style="left:30px;top:292px;width:213px">
    <h2>Underground Home</h2>
    <p>Our guide's family open the doors of their home and give you a guided tour of their dugout. See how a modern family live underground.</p>
  </section>
  <div class="photo" style="left:258px;top:290px;background:linear-gradient(135deg,#e8dccb,#b99b7e 60%,#c0493c)" role="img" aria-label="Photo of a bedroom in an underground dugout home"></div>

  <div class="photo" style="left:28px;top:364px;background:radial-gradient(circle at 45% 55%,#f6d21c 25%,#e9e9e9 45%)" role="img" aria-label="Photo of a yellow safety helmet"></div>
  <section class="stop" style="left:153px;top:364px;width:220px">
    <h2>Safety Gear</h2>
    <p>All safety gear will be provided for you including helmets and UHF radios. Your safety is our number one priority!</p>
  </section>

  <section class="stop right-text" style="left:30px;top:430px;width:213px">
    <h2>Opal Mining</h2>
    <p>We'll make our way down an underground mine where we'll show you the different techniques that modern miners use to extract this beautiful stone.</p>
  </section>
  <div class="photo" style="left:258px;top:433px;background:radial-gradient(circle at 45% 50%,#8a8c8e,#4a3d2a 45%,#9b7a3a)" role="img" aria-label="Photo of visitors walking through an underground mine tunnel"></div>

  <div class="photo" style="left:28px;top:514px;background:linear-gradient(160deg,#cfc3b0,#b8a78c)" role="img" aria-label="Aerial photo of cars driving through the opal fields"></div>
  <section class="stop" style="left:151px;top:512px;width:225px">
    <h2>Drive Through The Field</h2>
    <p style="font-size:8.4px">Making our way into town, via the opal fields, you'll get a front row seat for viewing our magical landscape that has been terraformed with over 100 years of mining. We might even stop at a scenic lookout on our way!</p>
  </section>

  <section class="stop right-text" style="left:30px;top:597px;width:213px">
    <h2>Noodling</h2>
    <p>Next we hit the noodling field to try and find our own opal. With our expert guide showing you how to find opal you'll be a pro in no time!</p>
  </section>
  <div class="photo" style="left:256px;top:595px;background:radial-gradient(ellipse at 50% 50%,#b5572a,#4f6b45 35%,#ececec 55%)" role="img" aria-label="Photo of a polished opal stone"></div>

  <div class="photo" style="left:28px;top:682px;background:linear-gradient(135deg,#6b6b6b,#d0d0d0 55%,#3e3e3e)" role="img" aria-label="Black and white photo of hands cutting and polishing opal"></div>
  <section class="stop" style="left:158px;top:680px;width:215px">
    <h2>Opal Cutting and Polishing</h2>
    <p>Next we hit the noodling field to try and find our own opal. With our expert guide showing you how to find opal you'll be a pro in no time!</p>
  </section>

  <footer class="footer">
    <svg width="24" height="16" viewBox="0 0 24 16" aria-hidden="true"><rect x="1" y="1" width="22" height="14" fill="none" stroke="#f15a24" stroke-width="1.6"/><path d="M1 1 L12 9 L23 1 M1 15 L9 7 M23 15 L15 7" fill="none" stroke="#f15a24" stroke-width="1.6"/></svg>
    <span>hello@trailalong.example</span>
    <svg class="phone" width="10" height="18" viewBox="0 0 10 18" aria-hidden="true"><path d="M7 1 C2 3 1 7 1 9 C1 11 2 15 7 17 L9 14 L6 12 C5 10 5 8 6 6 L9 4Z" fill="#f15a24"/></svg>
    <span>+15550100200</span>
  </footer>
</main>
</body>
</html>
```